Chewable Dog Supplements jar with lid

Below are some specifications of this project: 
There will be 6 different types of dog supplements in different jars, which will have different colors, or elements(dogs),  but will respect the same theme overall.  I attached some pictures below as a reference.
 The design I would like to create is for a label that will go around and on the top of a round plastic jar. The size of the product label is 25cm long and 8.5 cm high and on the top there is a circle that goes on the lid with the exact same design as on the front.
Some small pictures on the back with no Grain, Corn or Soy derivates  
 All products come in different shapes chews 
All products have 3 different headlines with their benefits that go on the front of the design.
All products have different flavors.
Regarding the text that will go on the back of the product, I can help with adding that to all products as long as we agree on how it looks. On the back I will need a space for a barcode, best before date, there should be 2 tables with ingredients and directions for use, and space for text under :Storage instructions, Warning, Description.

Target Market(s)

Europe

Industry/Entity Type

pet food

Requirements
Must have
• Trust signals ( Free from GMO, Natural ingredients, Free from artificial colouring) and a text box with the benefits of the product that I will provide.

```html
<!DOCTYPE html>
<html lang="en">
<head>
<meta charset="utf-8">
<title>Multivitamin Chews Label</title>
<link href="https://fonts.googleapis.com/css2?family=Rubik:wght@500;700;800;900&display=swap" rel="stylesheet">
<style>
  :root {
    --bg: #fcfcfd;
    --label-red: #d9333b;
    --label-red-light: #e2464c;
    --white: #ffffff;
    --ink: #1c1c1c;
    --sky: #9fd0ef;
    --maroon: #5e1830;
    --flavor-fill: #f3e4e6;
  }
  * { margin: 0; padding: 0; box-sizing: border-box; }
  html, body { width: 963px; height: 1200px; overflow: hidden; background: var(--bg); }
  body { position: relative; font-family: "Rubik", sans-serif; }

  .label {
    position: absolute; left: 224px; top: 330px; width: 516px; height: 550px;
    background: linear-gradient(90deg, var(--label-red-light) 0%, var(--label-red) 55%, #d02e36 100%);
  }
  .brand {
    position: absolute; top: 62px; left: 0; width: 100%;
    display: flex; flex-direction: column; align-items: center; gap: 10px;
  }
  .brand-dot { width: 30px; height: 30px; border-radius: 50%; background: var(--ink); }
  .brand-name { font-weight: 700; font-size: 12px; letter-spacing: 2.5px; color: var(--ink); }
  .art { position: absolute; left: 0; top: 0; width: 516px; height: 550px; }
  .benefits { font-family: "Rubik", sans-serif; font-weight: 800; font-size: 13px; fill: var(--white); }
  .flavor { font-family: "Rubik", sans-serif; font-weight: 800; font-size: 15px; fill: var(--maroon); letter-spacing: 1px; }

  .title {
    position: absolute; left: 0; width: 100%; text-align: center;
    color: var(--ink); font-weight: 900; line-height: 1;
  }
  .title-top { top: 208px; font-size: 50px; letter-spacing: -0.5px; }
  .title-main { top: 262px; font-size: 104px; letter-spacing: 1px; }

  .audience {
    position: absolute; left: 133px; top: 378px; width: 246px; height: 38px;
    background: var(--sky); border-radius: 6px;
    display: flex; align-items: center; justify-content: center;
    color: var(--white); font-weight: 700; font-size: 23px;
  }

  .count {
    position: absolute; left: 40px; top: 440px; text-align: center;
    color: var(--white); font-weight: 800; line-height: 1.05;
  }
  .count-num { font-size: 30px; }
  .count-unit { font-size: 18px; }

  .trust { position: absolute; left: 128px; top: 448px; display: flex; gap: 12px; align-items: center; }
  .trust-badge {
    background: var(--white); border: 2px solid var(--ink); border-radius: 50%;
    display: flex; align-items: center; justify-content: center; text-align: center;
    font-weight: 800; font-size: 9.5px; line-height: 1.05; color: var(--ink);
    padding: 4px 8px;
  }
  .trust-badge.wide { width: 74px; height: 48px; }
  .trust-badge.small { width: 52px; height: 48px; }
  .trust-badge.mid { width: 76px; height: 38px; }

  .weight {
    position: absolute; left: 0; width: 100%; top: 516px; text-align: center;
    color: var(--white); font-weight: 800; font-size: 17px;
  }
</style>
</head>
<body>
  <main class="label">
    <svg class="art" viewBox="0 0 516 550">
      <defs>
        <path id="benefit-arc" d="M30 268 C 32 200 90 162 200 156 L 482 152"/>
        <path id="flavor-top" d="M394 460 A40 40 0 0 1 474 460"/>
        <path id="flavor-bottom" d="M382 460 A52 52 0 0 0 486 460"/>
      </defs>
      <path class="speech-bubble" fill="#ffffff"
        d="M120 184 C 200 172 320 172 430 178 C 478 182 480 214 474 250 C 468 300 462 340 440 352 C 420 362 410 372 398 392 C 404 372 400 362 380 364 C 290 370 180 372 90 366 C 52 362 46 330 48 290 C 50 240 62 198 120 184 Z"/>
      <text class="benefits"><textPath href="#benefit-arc" textLength="470" lengthAdjust="spacingAndGlyphs">STRONG IMMUNITY HIP AND JOINT SUPPORT SKIN AND COAT HEALTH</textPath></text>
      <circle cx="434" cy="460" r="50" fill="none" stroke="#5e1830" stroke-width="3"/>
      <circle cx="434" cy="460" r="28" fill="#f3e4e6" role="img" aria-label="Small dog character illustration"/>
      <text class="flavor" text-anchor="middle"><textPath href="#flavor-top" startOffset="50%">SALMON</textPath></text>
      <text class="flavor" text-anchor="middle"><textPath href="#flavor-bottom" startOffset="50%">FLAVOR</textPath></text>
    </svg>

    <div class="brand">
      <span class="brand-dot"></span>
      <span class="brand-name">PAWVITA</span>
    </div>

    <h1 class="title title-top">MULTIVITAMIN</h1>
    <h2 class="title title-main">CHEWS</h2>

    <div class="audience">SUPPORT FOR DOGS</div>

    <div class="count">
      <div class="count-num">60</div>
      <div class="count-unit">CHEWS</div>
    </div>

    <div class="trust">
      <span class="trust-badge wide">FREE FROM ARTIFICIAL COLOURING</span>
      <span class="trust-badge small">FREE FROM GMO</span>
      <span class="trust-badge mid">NATURAL INGREDIENTS</span>
    </div>

    <p class="weight">NET WT 5.29 OZ(150G)</p>
  </main>
</body>
</html>
```